THis will be a flyer to post around town for our Big Buck Contest. Here are the rules (which can be in small print). It should appeal to hunters. We are in Texas.

2014-2015 BIG BUCK CONTEST
OFFICIAL RULES:
1. Eligible hunters must be signed in and have $20 entry fee paid between November 1, 2014 - ____________________. Hunters may enter online @ www.brindlecreekhub.org or stop by The Pecan Hollow Area Chamber of Commerce for an entry form @ 418 E. Juniper Ave. on the square in Pecan Hollow.
2. Deer must be a whitetail buck killed during the general hunting season.
3. Bucks killed within a deer-proof fence or any other confined areas are not eligible to enter contest. Bucks that were EVER kept inside a pen for breeding purposes or any other reason are NOT allowed. Bucks that are tagged or tattooed are NOT allowed. Bucks cannot have been raised in a fenced in area and released. Bucks considered tame, domesticated or pet are NOT allowed.
4. Bucks must be properly tagged according to Texas State Law when brought in for measurement. Hunter must present valid hunting license and contest entry for to the official measurer.
5. Hunters attempting to cheat in the BIG BUCK CONTEST or violating Texas Game Laws are disqualified and barred from entering this contest for a period of time to be determined by the contest committee.
6. NO MORE than 1 prize will be awarded to any registered hunter. A hunter’s second buck is valid if it outscores first buck.
7. All entries must be brought in by the rightful. Any attempts to alter or enhance the horns in any from will be grounds for disqualification WITHOUT refund.
8. You must enter your buck in the contest within 72 hours of kill, unless prior arrangements have been made.

Measurements Guidelines:
For measurement, the hunter must bring the ENTIRE BODY of the field dressed animal to one of the official measurers.

Total $25.00
_____ Check ______ Money Order _____ Cashier Check
*** Please DO NOT DROP OFF OF MAIL CASH***

DROP OFF AT OR MAIL TO:

The Pecan Hollow Area Chamber of Commerce
418 E. Juniper Ave
Pecan Hollow, TX 76312

PRIZES:
1. Velmon Strouth Taxidermy - Shoulder Mount (donated)
>
> 2. 45 quart Kodo cooler sponsored by Ridgeway Timber and Fellowship of the Plains
>
> 3. 500 lbs of deer corn sponsored by Tanning Feed.

Target Market(s)

Texas deer hunters

Industry/Entity Type

Town

Requirements
Must have
• rules
• Fee amount $20
• Pecan Hollow Area Chamber of Commerce

```html
<!DOCTYPE html>
<html lang="en">
<head>
<meta charset="utf-8">
<title>2014-2015 Big Buck Contest</title>
<link rel="stylesheet" href="https://fonts.googleapis.com/css2?family=Anton&family=Open+Sans:wght@400;600;700;800&display=swap">
<style>
:root{
  --chamber-green:#0f5a2c;
  --title-lime:#cfe04a;
  --title-shadow:#2a2a12;
  --texas-red:#c8102e;
  --panel-edge:#6f8f2a;
  --panel-mid:#c9c7a3;
  --ink:#1d1d12;
  --autumn-a:#c9772a;
  --autumn-b:#e9b25a;
  --autumn-c:#8a4a1c;
}
*{box-sizing:border-box;margin:0;padding:0}
html,body{width:927px;height:1200px;overflow:hidden;background:#fff}
.flyer{position:relative;width:927px;height:1200px;overflow:hidden;font-family:"Open Sans",Arial,sans-serif;color:var(--ink)}
.autumn-scene{position:absolute;left:0;top:315px;width:927px;height:885px;
  background:radial-gradient(ellipse at 80% 30%,var(--autumn-b),transparent 55%),
  radial-gradient(ellipse at 15% 80%,var(--autumn-c),transparent 60%),
  linear-gradient(180deg,var(--autumn-a),#d4923c 50%,#b8662a)}
.camo-band{position:absolute;left:0;top:0;width:927px;height:315px;
  background:radial-gradient(circle at 20% 60%,#5e6b3a,transparent 40%),
  radial-gradient(circle at 70% 30%,#7b6a48,transparent 45%),
  radial-gradient(circle at 90% 80%,#4b5a2c,transparent 40%),
  linear-gradient(135deg,#6b5a3e,#4a5230 50%,#7a6a4a)}
.chamber-mark{position:absolute;left:18px;top:15px;width:232px;height:143px;background:var(--chamber-green);
  display:flex;flex-direction:column;align-items:center;justify-content:center;gap:10px;color:#fff;text-align:center}
.chamber-mark .dot{width:44px;height:44px;border-radius:50%;background:#fff}
.chamber-mark .name{font-size:14px;font-weight:600;line-height:1.2;padding:0 12px}
.title-years,.title-main,.title-place{position:absolute;font-family:Anton,Impact,sans-serif;white-space:nowrap;line-height:1;font-weight:400}
.title-years{left:268px;top:58px;font-size:96px;letter-spacing:2px;color:var(--title-lime);
  transform:rotate(-8deg);transform-origin:left bottom;text-shadow:4px 4px 0 var(--title-shadow)}
.title-main{left:128px;top:170px;font-size:116px;color:var(--title-lime);
  transform:rotate(-7deg);transform-origin:left bottom;text-shadow:5px 5px 0 var(--title-shadow)}
.title-place{left:528px;top:246px;font-size:64px;letter-spacing:3px;color:var(--texas-red);text-shadow:3px 3px 0 #3a1a10}
.rules-panel{position:absolute;left:263px;top:337px;width:402px;height:851px;padding:12px 16px 0 16px;
  background:radial-gradient(ellipse at 50% 50%,var(--panel-mid) 35%,#a9b46a 70%,var(--panel-edge))}
.rules-panel h2{font-size:17px;font-weight:800;letter-spacing:1.5px;text-align:center;margin-bottom:6px}
.rules-panel h3{font-size:13.5px;font-weight:700;text-align:center;margin:4px 0 6px}
.rules-list,.prize-list{padding-left:22px;font-size:10.4px;line-height:1.38}
.rules-list li,.prize-list li{padding-left:6px}
.measure-note{font-size:10.4px;line-height:1.38;margin-left:-8px}
.payment{margin-left:-8px}
.total{font-size:13.5px;font-weight:700;margin:16px 0 12px}
.pay-option{display:flex;align-items:center;gap:6px;font-size:10.4px;margin:0 0 12px 6px}
.pay-option .box{width:14px;height:14px;border:1.3px solid var(--ink)}
.cash-warning{font-size:11.5px;font-weight:700;margin:-2px 0 18px}
.mail-to{text-align:center;font-size:11.5px;font-weight:700;line-height:1.5}
.mail-to h3{margin-bottom:6px}
.prizes{margin-top:14px}
.hunter-photo{position:absolute;left:685px;top:607px;width:226px;height:226px;
  background:linear-gradient(180deg,#9bbbd6 0%,#b9c7b5 45%,#8a8a6a 70%,#c8b795)}
.sponsor{position:absolute;background:#fff;display:flex;align-items:center;justify-content:center;gap:8px;
  font-weight:700;text-align:center;line-height:1.15;font-size:15px}
.sponsor-timber{left:687px;top:860px;width:220px;height:84px;background:#f1ece6;color:#c8202a}
.sponsor-fellowship{left:683px;top:975px;width:220px;height:75px;color:#1e3a7a}
.sponsor-grain{left:683px;top:1088px;width:220px;height:75px;color:#1e3a7a}
.sponsor .sq{width:18px;height:18px;background:currentColor;flex:none}
</style>
</head>
<body>
<main class="flyer">
  <div class="autumn-scene" role="img" aria-label="Autumn forest illustration with antlered deer among orange leaves"></div>
  <div class="camo-band" role="img" aria-label="Woodland camouflage pattern of bark and leaves"></div>

  <div class="chamber-mark">
    <span class="dot"></span>
    <span class="name">Pecan Hollow Area Chamber of Commerce</span>
  </div>

  <div class="title-years">2014-2015</div>
  <h1 class="title-main">BIG BUCK CONTEST</h1>
  <div class="title-place">TEXAS, USA</div>

  <section class="rules-panel">
    <h2>OFFICIAL RULES</h2>
    <ol class="rules-list">
      <li>Eligible hunters must be signed in and have $20 entry fee paid between November 1, 2014 - ____________________. Hunters may enter online @ www.brindlecreekhub.org or stop by The Pecan Hollow Area Chamber of Commerce for an entry form @ 418 E. Juniper Ave. on the square in Pecan Hollow.</li>
      <li>Deer must be a whitetail buck killed during the general hunting season.</li>
      <li>Bucks killed within a deer-proof fence or any other confined areas are not eligible to enter contest. Bucks that were EVER kept inside a pen for breeding purposes or any other reason are NOT allowed. Bucks that are tagged or tattooed are NOT allowed. Bucks cannot have been raised in a fenced in area and released. Bucks considered tame, domesticated or pet are NOT allowed.</li>
      <li>Bucks must be properly tagged according to Texas State Law when brought in for measurement. Hunter must present valid hunting license and contest entry for to the official measurer.</li>
      <li>Hunters attempting to cheat in the BIG BUCK CONTEST or violating Texas Game Laws are disqualified and barred from entering this contest for a period of time to be determined by the contest committee.</li>
      <li>NO MORE than 1 prize will be awarded to any registered hunter. A hunter’s second buck is valid if it outscores first buck.</li>
      <li>All entries must be brought in by the rightful. Any attempts to alter or enhance the horns in any from will be grounds for disqualification WITHOUT refund.</li>
      <li>You must enter your buck in the contest within 72 hours of kill, unless prior arrangements have been made.</li>
    </ol>
    <h3>Measurements Guidelines</h3>
    <p class="measure-note">For measurement, the hunter must bring the ENTIRE BODY of the field dressed animal to one of the official measurers.</p>

    <div class="payment">
      <p class="total">Total $25.00</p>
      <p class="pay-option"><span class="box"></span>Check</p>
      <p class="pay-option"><span class="box"></span>Money Order</p>
      <p class="pay-option"><span class="box"></span>Cashier Check</p>
      <p class="cash-warning"><em>IMPORTANT</em>: Please DO NOT DROP OFF OF MAIL CASH</p>
    </div>

    <div class="mail-to">
      <h3>DROP OFF AT OR MAIL TO:</h3>
      <p>The Pecan Hollow Area Chamber of Commerce<br>418 E. Juniper Ave<br>Pecan Hollow, TX 76312</p>
    </div>

    <div class="prizes">
      <h3>PRIZES:</h3>
      <ol class="prize-list">
        <li>Velmon Strouth Taxidermy - Shoulder Mount (donated)</li>
        <li>45 quart Kodo cooler sponsored by Ridgeway Timber and Fellowship of the Plains</li>
        <li>3. 500 lbs of deer corn sponsored by Tanning Feed.</li>
      </ol>
    </div>
  </section>

  <div class="hunter-photo" role="img" aria-label="Photo of a hunter kneeling beside a large whitetail buck in brush country"></div>

  <div class="sponsor sponsor-timber">Ridgeway Timber Company</div>
  <div class="sponsor sponsor-fellowship"><span class="sq"></span>Fellowship of the Plains</div>
  <div class="sponsor sponsor-grain"><span class="sq"></span>Hollis Grainworks</div>
</main>
</body>
</html>
```